New Body Mist 250 ml exclusive

We are excited to embark on a new project to design the packaging for body mist:
Amber Drizzle

We are looking for a design that is truly unique and stands out, with a touch of individuality that sets it apart. The design should be eye-catching and visually appealing, drawing attention even from a distance. We want the body mists to have a fun and attractive look that appeals to customers.

To help bring your design to life, we will provide the dimensions of the bottle, which has a capacity of 250ml. The bottle measures 13.3 cm in height and 4.9 cm in diameter (excluding the pump). Additionally, we will also provide the dimensions of the label, which measures 15.1 cm in height and 12.8 cm in width.

We believe that giving you the freedom to put your own unique touch and color choices will help create a truly standout design. We look forward to seeing your creative vision for our body mist.

We shared with you the logo of the body mist and some examples of models that we liked.

Please be informed that the project only includes one design and the remaining three will be completed and paid for through a 1on1 project with the winner of the contest.

Target Market(s)

Supermarket and perfumery stores

Industry/Entity Type

Cosmetics

Font styles to use
Serif

Requirements
Must have
• Uniqueness and attractiveness

```html
<!DOCTYPE html>
<html lang="en">
<head>
<meta charset="utf-8">
<title>Amber Drizzle – Body Mist Label</title>
<link rel="stylesheet" href="https://fonts.googleapis.com/css2?family=Josefin+Sans:wght@400&display=swap">
<style>
  :root {
    --page-bg: #f1f0f2;
    --label-lavender: #d9d2ec;
    --label-pink: #e6b6e6;
    --label-violet: #c79ad9;
    --label-mint: #d6f0dc;
    --label-butter: #f2ecc8;
    --panel-tint: rgba(226, 220, 240, 0.78);
    --frame-rose: #8c6b88;
    --name-plum: #4a3148;
  }
  html, body {
    margin: 0;
    padding: 0;
    width: 1200px;
    height: 1200px;
    overflow: hidden;
    background: var(--page-bg);
  }
  .canvas {
    position: relative;
    width: 1200px;
    height: 1200px;
    display: flex;
    align-items: center;
    justify-content: center;
  }
  .label {
    position: relative;
    width: 860px;
    height: 1014px;
    overflow: hidden;
    box-shadow: 0 18px 50px rgba(80, 60, 90, 0.12);
  }
  .label__marble {
    position: absolute;
    inset: 0;
    background:
      radial-gradient(ellipse 60% 40% at 78% 22%, var(--label-pink) 0%, transparent 70%),
      radial-gradient(ellipse 55% 35% at 30% 85%, var(--label-violet) 0%, transparent 70%),
      linear-gradient(90deg,
        var(--label-mint) 0%,
        var(--label-butter) 6%,
        var(--label-lavender) 18%,
        var(--label-lavender) 60%,
        var(--label-pink) 82%,
        var(--label-butter) 94%,
        var(--label-mint) 100%);
  }
  .label__emblem {
    position: absolute;
    left: 50%;
    top: 50%;
    width: 440px;
    height: 440px;
    transform: translate(-50%, -50%);
  }
  .label__emblem svg {
    position: absolute;
    inset: 0;
  }
  .label__name {
    position: absolute;
    inset: 0;
    display: flex;
    align-items: center;
    justify-content: center;
    margin: 0;
    font-family: "Josefin Sans", sans-serif;
    font-weight: 400;
    font-size: 34px;
    font-variant: small-caps;
    letter-spacing: 0.16em;
    color: var(--name-plum);
  }
</style>
</head>
<body>
  <main class="canvas">
    <section class="label">
      <div class="label__marble" role="img" aria-label="Pastel marbled swirl pattern in lavender, pink and iridescent mint"></div>
      <div class="label__emblem">
        <svg width="440" height="440" viewBox="0 0 440 440" aria-hidden="true">
          <rect x="0" y="0" width="440" height="440" fill="var(--panel-tint)"/>
          <rect x="2" y="2" width="436" height="436" fill="none" stroke="var(--frame-rose)" stroke-width="3"/>
        </svg>
        <h1 class="label__name">Amber Drizzle</h1>
      </div>
    </section>
  </main>
</body>
</html>
```